Business card design

I need my logo on this card, things I need the card to have on it
licensed and insured.
owner operators Derek & Milton Halvorsen
my phone number 5418237906
Disaster Recovery, Storm Damage Restoration, Proactive Disaster Plan Management, Roof Repair/Restoration Structural Repair and Reconstruction, Emergency Boarding and Tarping Service, Perimeter Fencing, Emergency Tree Removal,

```html
<!DOCTYPE html>
<html lang="en">
<head>
<meta charset="utf-8">
<title>Halvorsen's Construction – Business Card</title>
<link rel="stylesheet" href="https://fonts.googleapis.com/css2?family=Urbanist:wght@300;400;500;600;700&display=swap">
<style>
  :root {
    --backdrop: #404040;
    --paper: #ffffff;
    --ink: #000000;
    --brand-blue: #1296e8;
    --photo-light: #f1f1f1;
    --photo-mid: #d4d4d4;
    --white: #ffffff;
  }
  * { margin: 0; padding: 0; box-sizing: border-box; }
  html, body {
    width: 1200px; height: 1200px; overflow: hidden;
    background: var(--backdrop);
    font-family: "Urbanist", sans-serif;
  }
  .card {
    position: absolute; left: 276px;
    width: 957px; height: 608px;
    background: var(--paper);
    transform: scale(0.6772);
    transform-origin: top left;
    overflow: hidden;
    box-shadow: 0 26px 30px -14px rgba(0,0,0,0.55);
  }
  .card--front { top: 117px; }
  .card--back  { top: 600px; }
  .card-art { position: absolute; inset: 0; width: 100%; height: 100%; }

  /* front */
  .wordmark {
    position: absolute; left: 40px; width: 406px; top: 300px;
    text-align: center; color: var(--brand-blue); font-weight: 400;
  }
  .wordmark-name { font-size: 62px; line-height: 1; letter-spacing: 1px; }
  .wordmark-sub { font-size: 17px; letter-spacing: 11px; margin-top: 10px; }
  .owners {
    position: absolute; right: 60px; top: 496px;
    text-align: right; color: var(--white);
  }
  .owners-label { font-size: 35px; font-weight: 300; line-height: 44px; }
  .owners-names { font-size: 36px; font-weight: 600; line-height: 44px; }

  /* back */
  .services {
    position: absolute; left: 0; right: 0; top: 52px;
    text-align: center; color: var(--ink);
    font-size: 36px; font-weight: 400; line-height: 43px;
    list-style: none;
  }
  .back-name {
    position: absolute; left: 32px; top: 504px;
    color: var(--white); font-size: 28px; font-weight: 600;
  }
  .contact {
    position: absolute; right: 38px; top: 478px;
    text-align: right; color: var(--white);
  }
  .contact-badge { font-size: 33px; font-weight: 700; line-height: 44px; }
  .contact-phone {
    font-size: 43px; font-weight: 600; line-height: 56px;
    display: flex; align-items: center; justify-content: flex-end; gap: 8px;
  }
  .contact-phone svg { width: 36px; height: 36px; }
</style>
</head>
<body>

<section class="card card--front">
  <svg class="card-art" viewBox="0 0 957 608" aria-hidden="false">
    <defs>
      <linearGradient id="houseTone" x1="0" y1="0" x2="1" y2="1">
        <stop offset="0" stop-color="var(--photo-light)"/>
        <stop offset="1" stop-color="var(--photo-mid)"/>
      </linearGradient>
    </defs>
    <polygon role="img" aria-label="Black and white photograph of a two-storey house with dormers and a porch"
             points="297,0 957,0 957,480 617,480" fill="url(#houseTone)"/>
    <polygon class="accent-stripe" points="255,0 297,0 621,480 579,480" fill="var(--brand-blue)"/>
    <path class="footer-band" d="M70,608 L150,514 Q185,477 240,477 L772,477 Q792,477 808,460 L957,300 L957,608 Z" fill="var(--ink)"/>
  </svg>
  <div class="wordmark">
    <div class="wordmark-name">HALVORSEN'S</div>
    <div class="wordmark-sub">CONSTRUCTION L.L.C</div>
  </div>
  <div class="owners">
    <p class="owners-label">Owner operators</p>
    <p class="owners-names">Derek &amp; Milton HALVORSEN</p>
  </div>
</section>

<section class="card card--back">
  <svg class="card-art" viewBox="0 0 957 608">
    <defs>
      <linearGradient id="houseFaint" x1="0" y1="0" x2="1" y2="0.6">
        <stop offset="0" stop-color="#e9e9e9"/>
        <stop offset="0.6" stop-color="#f7f7f7"/>
        <stop offset="1" stop-color="#e6e6e6"/>
      </linearGradient>
    </defs>
    <rect role="img" aria-label="Faded photograph of a house among trees" x="0" y="0" width="957" height="608" fill="url(#houseFaint)"/>
    <polygon class="corner-black" points="0,326 0,608 334,608" fill="var(--ink)"/>
    <polygon class="corner-blue" points="260,544 957,346 957,608 334,608" fill="var(--brand-blue)"/>
  </svg>
  <ul class="services">
    <li>Disaster Recovery</li>
    <li>Storm Damage Restoration,</li>
    <li>Proactive Disaster Plan Management,</li>
    <li>Roof Repair/Restoration Structural</li>
    <li>Repair and Reconstruction,</li>
    <li>Emergency Boarding and Tarping Service,</li>
    <li>Perimeter Fencing,</li>
    <li>Emergency Tree Removal</li>
  </ul>
  <div class="back-name">HALVORSEN'S</div>
  <div class="contact">
    <p class="contact-badge">LICENSED AND INSURED</p>
    <p class="contact-phone">
      <svg viewBox="0 0 24 24" aria-hidden="true"><path fill="currentColor" d="M6.6 10.8c1.4 2.8 3.8 5.1 6.6 6.6l2.2-2.2c.3-.3.7-.4 1-.2 1.1.4 2.3.6 3.6.6.6 0 1 .4 1 1V20c0 .6-.4 1-1 1C10.6 21 3 13.4 3 4c0-.6.4-1 1-1h3.5c.6 0 1 .4 1 1 0 1.3.2 2.5.6 3.6.1.3 0 .7-.2 1l-2.3 2.2z"/></svg>
      541 823 7906
    </p>
  </div>
</section>

</body>
</html>
```